Stationery design for software development / consultancy company

We need stationary design based on company logo.

We are based in London, UK and we are providing integration solutions development / consultancy services for QVR integration projects across UK.

Our name refers two words - integration and grace - and it shows our clients our main specialization field and key characteristics of our solutions / products. We also would like to be associated with follow words: smart, reliable, unique.

Project delivery should include:
- Powerpoint template (needs to have a Cover Page, Table of Contents, 1-2 sample pages, and a Closing/Summary slide at the end)
- Letterhead A4 (Word template)
- Standard invoice A4 (Word template)
- With Compliments Slips A5 (Word template)
- Business card (adobe illustrator)

Attached is logo in vector (please use logo with white background!) and company details for printed stationery.

Target Market(s)

highly skilled IT professionals

Industry/Entity Type

Software

Requirements
Must have
• Clear background in all A4/A5 documents.
All text should be editable, i.e. I will need sources.
Nice to have
• I would prefer light, web 2.0 style colours, follow are in my main interest:
- combination of light grey and orange
- Logo colours
Should not have
• Please no watermarks on printed stationary

```html
<!DOCTYPE html>
<html lang="en">
<head>
<meta charset="utf-8">
<title>Corvane business card</title>
<link rel="stylesheet" href="https://fonts.googleapis.com/css2?family=Source+Sans+3:wght@400;600&display=swap">
<style>
  :root {
    --board-edge: #d9d9db;
    --board: #ffffff;
    --card-shadow: #dcdcde;
    --card-front: #ffffff;
    --card-back: #58585a;
    --ink: #3c3c3e;
    --ink-brand: #58585a;
    --accent-red: #c1272d;
    --accent-orange: #f39200;
    --rule: #dcdcdf;
  }
  * { margin: 0; padding: 0; box-sizing: border-box; }
  html, body { width: 1168px; height: 1200px; overflow: hidden; }
  body {
    background: var(--board-edge);
    font-family: "Source Sans 3", "Myriad Pro", Arial, sans-serif;
    color: var(--ink);
    position: relative;
  }
  .board {
    position: absolute; left: 25px; top: 25px; width: 1119px; height: 1148px;
    background: var(--board); border-radius: 67px;
  }
  .card { position: absolute; border-radius: 20px; }
  .card-shadow { position: absolute; border-radius: 20px; background: var(--card-shadow); }
  .card--front { left: 140px; top: 175px; width: 584px; height: 359px;
    background: var(--card-front); border: 1.5px solid #c8c8ca; }
  .card--back { left: 451px; top: 629px; width: 586px; height: 357px; background: var(--card-back); }
  .shadow--front { left: 154px; top: 189px; width: 584px; height: 359px; }
  .shadow--back { left: 465px; top: 643px; width: 586px; height: 357px; }

  .brand { position: absolute; display: flex; align-items: center; gap: 10px;
    font-weight: 600; line-height: 1; letter-spacing: -0.5px; }
  .brand-dot { border-radius: 50%; background: var(--accent-orange); flex: none; }
  .brand--front { left: 256px; top: 50px; font-size: 54px; color: var(--ink-brand); }
  .brand--front .brand-dot { width: 44px; height: 44px; }
  .brand--back { left: 142px; top: 143px; font-size: 62px; color: #ffffff; }
  .brand--back .brand-dot { width: 50px; height: 50px; }

  .person-name, .company-name { position: absolute; top: 128px; font-size: 25px;
    color: var(--accent-red); line-height: 1; }
  .person-name { left: 33px; }
  .company-name { left: 257px; }
  .person-role { position: absolute; right: 376px; top: 166px; font-size: 16px; line-height: 1; }

  .address { position: absolute; left: 258px; top: 166px; font-size: 16px; line-height: 21.5px; }
  .contact { position: absolute; left: 258px; top: 250px; font-size: 16px; line-height: 22px;
    border-collapse: collapse; }
  .contact td { padding: 0; }
  .contact .label { width: 70px; }

  .view-label { position: absolute; font-size: 25px; color: #111; line-height: 1; }
  .view-label--front { left: 104px; top: 556px; }
  .view-label--back { left: 406px; top: 1003px; }
  .view-rule { position: absolute; height: 5px; background: var(--rule); }
  .view-rule--front { left: 180px; top: 570px; width: 557px; }
  .view-rule--back { left: 475px; top: 1018px; width: 574px; }
</style>
</head>
<body>
  <div class="board"></div>

  <div class="card-shadow shadow--front"></div>
  <section class="card card--front" aria-label="Card front">
    <div class="brand brand--front"><span class="brand-dot"></span><span>corvane</span></div>
    <div class="person-name">Daniel Orrin</div>
    <div class="person-role">Director</div>
    <div class="company-name">Corvane Limited</div>
    <div class="address">42 Elm Court<br>88 Kestrel Avenue - London<br>SE9 4QT - United Kingdom</div>
    <table class="contact">
      <tr><td class="label">Web</td><td>www.corvane.co.uk</td></tr>
      <tr><td class="label">Email</td><td>daniel@corvane.co.uk</td></tr>
      <tr><td class="label">Tel</td><td>+44(0)121 555 0148</td></tr>
      <tr><td class="label">Mob</td><td>+44(0)7700900361</td></tr>
    </table>
  </section>
  <div class="view-label view-label--front">Front</div>
  <div class="view-rule view-rule--front"></div>

  <div class="card-shadow shadow--back"></div>
  <section class="card card--back" aria-label="Card back">
    <div class="brand brand--back"><span class="brand-dot"></span><span>corvane</span></div>
  </section>
  <div class="view-label view-label--back">Back</div>
  <div class="view-rule view-rule--back"></div>
</body>
</html>
```